Building Servicess

We need a new business card design for a company. We specialise in: Electrical/Site temporary electrics, Data/Network Installation, Passive Fire Protection

Industry/Entity Type

Construction

Contact Information for Business Card

Services provided as detailed on project description

Font styles to use
Serif

Colors
0054AA
0677BA
7BADD7
CADEEF
E8F1F8
00AB8E
00BBA5
67D7C9
C6EFE9
E9F9F6
EB3D1F
EC4F4E
F09395
F8D3D4
FCEDEE

Requirements
Must have
• Company logo-contact details-phone numbers

```html
<!DOCTYPE html>
<html lang="en">
<head>
<meta charset="utf-8">
<title>Calderline Services Ltd – Business Card</title>
<link rel="stylesheet" href="https://fonts.googleapis.com/css2?family=PT+Serif:wght@400;700&display=swap">
<style>
  :root {
    --backdrop: #d9d9d9;
    --card-white: #ffffff;
    --brand-blue: #0d77bd;
    --tab-grey: #7b7c7e;
    --ink: #222222;
    --muted: #555555;
  }
  * { box-sizing: border-box; margin: 0; padding: 0; }
  html, body {
    width: 1200px; height: 1059px; overflow: hidden;
    background: var(--backdrop);
    font-family: "PT Serif", Georgia, serif;
  }
  .canvas { position: relative; width: 1200px; height: 1059px; }

  .card { position: absolute; border-radius: 21px; overflow: hidden; }
  .card-front { left: 256px; top: 100px; width: 688px; height: 391px; background: var(--card-white); }
  .card-back { left: 253px; top: 537px; width: 694px; height: 394px; background: var(--brand-blue); }

  .edge-strip { position: absolute; right: 0; width: 13px; background: var(--brand-blue); }
  .edge-strip.top { top: 0; height: 170px; border-radius: 0 0 0 6px; }
  .edge-strip.bottom { top: 219px; bottom: 0; border-radius: 6px 0 0 0; }
  .edge-tab { position: absolute; right: 0; top: 177px; width: 13px; height: 39px; background: var(--tab-grey); border-radius: 6px 0 0 6px; }

  .brand-name {
    position: absolute; left: 27px; top: 116px;
    font-weight: 700; font-size: 22px; line-height: 28px;
    color: var(--brand-blue); letter-spacing: 0.4px; text-transform: uppercase;
    white-space: nowrap;
  }

  .services {
    position: absolute; right: 46px; top: 40px; text-align: right;
    list-style: none; font-size: 14px; line-height: 21px; color: var(--muted);
  }
  .services li::after { content: ""; display: inline-block; width: 6px; height: 6px; margin-left: 8px; background: var(--brand-blue); vertical-align: middle; }

  .holder { position: absolute; right: 46px; top: 172px; text-align: right; }
  .holder-name { font-weight: 700; font-size: 23px; color: var(--brand-blue); letter-spacing: 0.6px; line-height: 28px; }
  .holder-role { font-size: 15px; color: var(--ink); line-height: 20px; }

  .address { position: absolute; left: 27px; top: 226px; font-size: 15px; line-height: 20.5px; color: var(--ink); font-style: normal; }

  .contact-list { position: absolute; left: 27px; top: 277px; list-style: none; font-size: 15px; color: var(--ink); }
  .contact-list li { display: flex; align-items: center; height: 20.5px; }
  .contact-list svg { width: 12px; height: 12px; margin-right: 5px; fill: var(--brand-blue); flex: none; }

  .back-name {
    position: absolute; left: 0; right: 0; top: 200px; text-align: center;
    font-weight: 700; font-size: 38px; line-height: 46px;
    color: var(--card-white); letter-spacing: 1px; text-transform: uppercase;
    white-space: nowrap;
  }
</style>
</head>
<body>
<main class="canvas">
  <section class="card card-front" aria-label="Business card front">
    <div class="edge-strip top"></div>
    <div class="edge-tab"></div>
    <div class="edge-strip bottom"></div>

    <ul class="services">
      <li>Electrical &amp; Temporary Site Electrics</li>
      <li>Data &amp; Network Installation</li>
      <li>Passive Fire Protection</li>
    </ul>

    <div class="brand-name">Calderline Services Ltd</div>

    <div class="holder">
      <p class="holder-name">DANIEL MORROW</p>
      <p class="holder-role">Managing Director</p>
    </div>

    <address class="address">
      418 Calder Mill Road.<br>
      Westbrook, AB 50210
    </address>

    <ul class="contact-list">
      <li>
        <svg viewBox="0 0 12 12" aria-hidden="true"><path d="M3 0h6a1 1 0 0 1 1 1v10a1 1 0 0 1-1 1H3a1 1 0 0 1-1-1V1a1 1 0 0 1 1-1zm0.5 1.5v7.5h5V1.5zM6 9.6a.7.7 0 1 0 0 1.4.7.7 0 0 0 0-1.4z"/></svg>
        07700900418
      </li>
      <li>
        <svg viewBox="0 0 12 12" aria-hidden="true"><path d="M2.4 0.6l1.8 2.2-1 1.2c.7 1.6 2 2.9 3.6 3.6l1.2-1 2.2 1.8-.9 2c-4.5-.2-8.3-4-8.5-8.5z"/></svg>
        020 7946 0321
      </li>
      <li>
        <svg viewBox="0 0 12 12" aria-hidden="true"><path d="M0 2h12v1.2L6 7 0 3.2zM0 4.6l6 3.8 6-3.8V10H0z"/></svg>
        info@calderlineltd.com
      </li>
      <li>
        <svg viewBox="0 0 12 12" aria-hidden="true"><path d="M6 0a6 6 0 1 0 0 12A6 6 0 0 0 6 0zm0 1.2c.9 0 1.8 2 1.9 4.2H4.1C4.2 3.2 5.1 1.2 6 1.2zM1.3 5.4h1.8c0-1.4.4-2.7.9-3.6a4.8 4.8 0 0 0-2.7 3.6zm0 1.2a4.8 4.8 0 0 0 2.7 3.6c-.5-.9-.9-2.2-.9-3.6zm2.8 0h3.8C7.8 8.8 6.9 10.8 6 10.8S4.2 8.8 4.1 6.6zm4.8 0c0 1.4-.4 2.7-.9 3.6a4.8 4.8 0 0 0 2.7-3.6zm1.8-1.2A4.8 4.8 0 0 0 8 1.8c.5.9.9 2.2.9 3.6z"/></svg>
        www.calderlineltd.com
      </li>
    </ul>
  </section>

  <section class="card card-back" aria-label="Business card back">
    <div class="back-name">Calderline Services Ltd</div>
  </section>
</main>
</body>
</html>
```